New Poster Design Project

Make an out standing A2 poster with below information,it is out first edition!Use the Attached image as background,Thanx!

Tolvik Meridian Arts Gathering
16 - 22 June 2014
Www.tmagfest.example

Creating a new vision of Africa through African Arts and Culture

Guest speakers / Artists

Delphine Korrato-Væstrup (S.A)
Tekle Berhanu Woldesan (Ethio)
Ronny Bastien-Kolo (Uganda)
Håkon Lunde (Nor)
Velvet Drum Collective (Zim)
Kalumbero Band (Moz,Nor,Swe & Zim)
Dj Zoto Zoto with Afro beats (Ghana/UK )
Dj Marquee/Storm Duchess with collage mix (Bergen)

@ Cafe Lutembe, Nordvik Global Heritage House (Nghh) Helsebrygga,Kjøpmannsplassen,Lindehagen & Vevergangen gate

Mon-Thur
Free entry,food & drinks served

Fri - Entry by donation & Sat - Tmagfest closing ceremony (100kr)
Updates

Project Deadline Extended

Project Deadline Extended
Reason: I made a mistake on extending time on this project now I can not reverse the extended time aaarrrr!!!I really dont have time,The poster should be all over the place by now since Im left with a couple of days away to the festival!!!I need someone to QuickFix me a A2 top notch poster in No time...my deadline is NOW NOW,LATEST Wednesday 21 May 2014,Thanx!

Industry/Entity Type

Cafe

Requirements
Must have
• sponsors logo
Nice to have
• Symbols
Should not have

```html
<!DOCTYPE html>
<html lang="en">
<head>
<meta charset="utf-8">
<title>Tolvik Meridian Arts Gathering 2014</title>
<link href="https://fonts.googleapis.com/css2?family=Yanone+Kaffeesatz:wght@300;400;500&family=Montserrat:wght@400;500&display=swap" rel="stylesheet">
<style>
  :root {
    --paper: #ffffff;
    --frame: #8a8a8a;
    --ink-dark: #1f1712;
    --sepia-mid: #6b5545;
    --sepia-light: #c9b7a3;
    --title-blue: #6f90b2;
    --accent-orange: #e07b33;
    --dancer-orange: #c2602a;
    --text-light: #f4efe8;
    --strip-red: #d0402f;
    --sponsor-ink: #2a2a2a;
  }
  * { box-sizing: border-box; margin: 0; padding: 0; }
  html, body { width: 843px; height: 1200px; overflow: hidden; background: var(--paper); }
  .poster {
    position: relative; width: 843px; height: 1200px;
    background: var(--paper);
    font-family: "Yanone Kaffeesatz", "Arial Narrow", sans-serif;
    color: var(--text-light);
  }
  .poster-panel {
    position: absolute; left: 13px; top: 12px; width: 817px; height: 1165px;
    border: 1px solid var(--frame); background: var(--paper); overflow: hidden;
  }
  .hero-photo {
    position: absolute; left: 0; top: 0; width: 100%; height: 1063px;
    background:
      radial-gradient(ellipse 38% 55% at 60% 55%, var(--sepia-light) 0%, var(--sepia-mid) 45%, transparent 80%),
      radial-gradient(ellipse 20% 14% at 62% 12%, #e9e4dc 0%, transparent 100%),
      linear-gradient(180deg, #2a1f18 0%, var(--ink-dark) 100%);
  }
  .brand { position: absolute; left: 22px; top: 12px; width: 160px; }
  .brand-name {
    font-family: "Montserrat", sans-serif; font-weight: 400; font-size: 36px;
    letter-spacing: 19px; color: var(--title-blue); line-height: 1;
  }
  .brand-square { display: block; width: 150px; height: 58px; margin-top: 8px; background: #000; }
  .festival-name { position: absolute; left: 8px; top: 148px; font-size: 24px; font-weight: 400; }
  .festival-date { position: absolute; left: 17px; top: 177px; font-size: 24px; color: var(--accent-orange); }
  .festival-web { position: absolute; left: 17px; top: 207px; font-size: 21px; }
  .tagline {
    position: absolute; left: 0; top: 262px; color: var(--title-blue);
    font-size: 33px; font-weight: 400; line-height: 41px;
  }
  .dancers { position: absolute; left: 36px; top: 445px; width: 76px; height: 92px; background: var(--dancer-orange); }
  .lineup-title { position: absolute; left: 622px; top: 516px; font-size: 23px; }
  .lineup { position: absolute; left: 578px; top: 583px; list-style: none; font-size: 18px; line-height: 20px; }
  .lineup li { margin-bottom: 25.5px; }
  .lineup li::before { content: "– "; }
  .lineup .indent { display: block; padding-left: 26px; }
  .venue { position: absolute; right: 44px; top: 1000px; font-size: 18px; text-align: right; }
  .venue-streets { position: absolute; right: 4px; top: 1037px; font-size: 18px; }
  .entry-bar {
    position: absolute; left: 0; top: 1063px; width: 100%; height: 18px;
    background: var(--ink-dark); color: var(--strip-red);
    font-size: 15px; line-height: 18px; padding-left: 32px; white-space: nowrap;
  }
  .sponsors {
    position: absolute; left: 0; top: 1081px; width: 100%; height: 84px;
    display: flex; align-items: center; background: var(--paper);
  }
  .sponsors-label {
    width: 28px; height: 84px; display: flex; align-items: center; justify-content: center;
    color: var(--strip-red); font-size: 18px; writing-mode: vertical-rl; transform: rotate(180deg);
  }
  .sponsor-list { flex: 1; display: flex; justify-content: space-around; align-items: center; }
  .sponsor {
    display: flex; flex-direction: column; align-items: center; gap: 4px;
    font-size: 15px; color: var(--sponsor-ink); text-align: center; max-width: 120px; line-height: 1;
  }
  .sponsor-dot { width: 36px; height: 36px; border-radius: 50%; background: var(--accent-orange); }
  .sponsor-dot.red { background: var(--strip-red); }
  .sponsor-dot.gold { background: #c29a3a; }
</style>
</head>
<body>
<div class="poster">
  <div class="poster-panel">
    <div class="hero-photo" role="img" aria-label="Sepia photograph of a smiling woman in a white head wrap, seated cross-legged and leaning on a carved thumb piano"></div>

    <div class="brand">
      <div class="brand-name">TMAG</div>
      <span class="brand-square"></span>
    </div>

    <h1 class="festival-name">Tolvik Meridian Arts Gathering</h1>
    <p class="festival-date">16 - 22 June 2014</p>
    <p class="festival-web">www.tmagfest.example</p>

    <h2 class="tagline">Creating<br>New vision of Africa<br>through<br>African Arts and Culture</h2>

    <div class="dancers" role="img" aria-label="Orange silhouette of three dancing figures"></div>

    <h3 class="lineup-title">Guest speakers / Artists</h3>
    <ul class="lineup">
      <li>Delphine Korrato-Væstrup (S.A)</li>
      <li>Tekle Berhanu Woldesan (Ethio)</li>
      <li>Ronny Bastien-Kolo (Uganda)</li>
      <li>Håkon Lunde (Nor)</li>
      <li>Velvet Drum Collective (Zim)</li>
      <li>Kalumbero Band (Moz,Nor,Swe &amp; Zim)</li>
      <li>Dj Zoto Zoto with Afro beats (Ghana/UK )</li>
      <li>Dj Marquee/Storm Duchess<span class="indent">with collage mix (Bergen)</span></li>
    </ul>

    <p class="venue">@ Cafe Lutembe, Nordvik Global Heritage House (Nghh)</p>
    <p class="venue-streets">Helsebrygga,Kjøpmannsplassen,Lindehagen &amp; Vevergangen gate</p>

    <p class="entry-bar">Mon-Thur &nbsp;&nbsp;&nbsp; -Free entry,food and drinks served &nbsp; -Fri - Entry by donation &amp; Sat - Tmagfest closing ceremony (100kr)</p>

    <footer class="sponsors">
      <div class="sponsors-label">Sponsors</div>
      <div class="sponsor-list">
        <div class="sponsor"><span class="sponsor-dot"></span>Mbeya Dance Circle</div>
        <div class="sponsor"><span class="sponsor-dot gold"></span>Dugnadshuset</div>
        <div class="sponsor"><span class="sponsor-dot red"></span>Nordvik Heritage House</div>
        <div class="sponsor"><span class="sponsor-dot gold"></span>Tolvik Kommune</div>
        <div class="sponsor"><span class="sponsor-dot"></span>kraftsenteret.example</div>
        <div class="sponsor"><span class="sponsor-dot"></span>kunstfond.example</div>
      </div>
    </footer>
  </div>
</div>
</body>
</html>
```